Keelbrook Vault Holdings Needs A Website

We are looking for a website for a new company. 4 Pages

Needs to be responsive and mobile friendly for all browsers and coded for both Android & IOS. SEO is also important.

Website Brief – Keelbrook Vault Holdings
Domain: www.keelbrookvault.net
Email: info@keelbrookvault.net
Phone: to be inserted later
Address: 40837 52 Ave, Edmonton, AB T6K 3R8
Platform: WordPress (recommended for flexibility, SEO tools, and ease of editing)
Requirements:
• Responsive & mobile-friendly (Android & iOS)
• Cross-browser compatibility
• Fast page load speed
• SEO optimized for storage development, management, and investment keywords
• Easy in-house editing after launch
• Professional, modern, trust-driven design reflecting expertise, reliability, and innovation
________________________________________
Pages
1. HOME
Purpose: Quickly communicate who Keelbrook Vault Holdings is and why they’re the best choice for designing, building, leasing, and managing self storage facilities.
Content Highlights:
• Hero Section: Large, bold image of a modern self storage facility with headline:
"From Concept to Capacity – Your Self Storage Experts"
• Subheadline: “Keelbrook Vault Holdings delivers turnkey design, construction, leasing, and management services for profitable self storage operations.”
• Quick Service Icons:
o Facility Design & Development
o Construction & Build Management
o Lease-Up & Marketing
o Ongoing Facility Management
• Call to Action Button: “LEARN MORE” → links to ABOUT US page.
• Featured Project Highlights: Showcase a few completed or current projects with photos and stats.
• Contact Banner: “Ready to build your next self storage project? Let’s talk.” → CONTACT page.
2. ABOUT US
Purpose: Build credibility, showcase experience, and explain the value proposition.
Content Highlights:
• Who We Are: Overview of Keelbrook Vault Holdings’ history, mission, and team expertise.
• Our Approach: End-to-end process from site selection to occupancy.
• Why Choose Us:
o Industry expertise in self storage
o Proven track record in lease-up success
o Strong vendor and contractor network
3. SERVICES
Purpose: Detail all service offerings with clarity and authority.
Sections:
• Design & Development: Market analysis, site planning, and architectural design.
• Construction Management: Overseeing timelines, budgets, and quality control.
• Lease-Up Strategy: Marketing, promotions, and occupancy acceleration.
• Ongoing Facility Management: Staffing, maintenance, revenue optimization.

4. CONTACT
Purpose: Provide simple, direct ways to connect.
Content Highlights:
• Contact Form (Name, Email, Phone, Message)
• Direct Email: info@keelbrookvault.net
• Phone (if applicable)
• Google Map embed (if there’s a head office location)
• CTA: “Let’s Build Your Storage Success Story.”
Design & Technical Notes
• Visual Style: Clean, modern, bold typography, professional color palette (to be based on branding), strong imagery of self storage facilities.
• Performance: Image compression, caching, responsive scaling.
• SEO Targets: “Self storage facility developer,” “self storage construction,” “self storage management company,” “lease-up services for self storage.”

WordPress or Joomla – must be desktop and mobile friendly with fast page load speed. Need the ability to edit ourselves.

Use pantone colours - #033c5a – dark blue
#2baadf – light blue

```html
<!DOCTYPE html>
<html lang="en">
<head>
<meta charset="utf-8">
<title>Keelbrook Vault Holdings – Self Storage Experts</title>
<link href="https://fonts.googleapis.com/css2?family=Montserrat:ital,wght@0,400;0,500;0,600;0,700;1,400&display=swap" rel="stylesheet">
<style>
:root{
  --dark:#033c5a;
  --light:#2baadf;
  --ink:#3d4a55;
  --mist:#e2e8ec;
  --white:#ffffff;
}
*{box-sizing:border-box;margin:0;padding:0}
html,body{width:1200px;height:3336px;overflow:hidden}
body{position:relative;background:var(--white);font-family:'Montserrat',sans-serif;color:var(--ink)}
.abs{position:absolute}
a{color:inherit;text-decoration:none}
.btn{position:absolute;display:flex;align-items:center;justify-content:center;background:var(--light);color:var(--white);border-radius:8px;font-size:16px;font-weight:500}
.brand{font-weight:600;color:var(--white);letter-spacing:.2px}

/* header */
.site-header{position:absolute;left:0;top:0;width:1200px;height:85px;background:var(--dark);z-index:3}
.site-header .brand{position:absolute;left:74px;top:30px;font-size:22px}
.nav a{position:absolute;top:32px;font-size:16px;color:var(--white)}
.nav .active{font-weight:700}
.nav .underline{position:absolute;left:698px;top:80px;width:57px;height:5px;background:var(--light)}

/* hero */
.hero-panel{position:absolute;left:52px;top:201px;width:576px;height:288px;background:rgba(255,255,255,.85)}
.hero-title{position:absolute;left:78px;top:220px;color:var(--dark);line-height:1.25}
.hero-title .lead{display:block;font-size:38px;font-weight:400}
.hero-title .strong{display:block;font-size:38px;font-weight:700}
.hero-text{position:absolute;left:78px;top:336px;width:486px;font-size:16px;line-height:23px;color:#1f2a33;text-align:justify}

/* section headings */
.section-title{position:absolute;left:0;width:1200px;text-align:center;font-size:39px;font-weight:600;color:var(--dark)}
.section-title span{color:var(--light)}
.roof{position:absolute;left:568px;width:64px;height:22px}

.intro{position:absolute;left:190px;top:889px;width:820px;text-align:center;font-size:15px;line-height:23px}

.service-title{position:absolute;font-size:17px;font-weight:600;line-height:21px;color:var(--dark)}
.service-title.alt{color:var(--light)}
.service-note{position:absolute;font-size:12px;font-style:italic;line-height:17px;color:#55616b}

/* projects */
.projects{position:absolute;left:0;top:1447px;width:1200px;height:707px;background:var(--mist)}
.project{position:absolute;top:1648px;width:448px;height:342px;border-radius:18px;overflow:hidden}
.project .photo{position:absolute;inset:0}
.project .caption{position:absolute;left:21px;top:248px;width:406px;height:72px;background:var(--white);border-radius:8px}
.caption h3{position:absolute;left:16px;top:14px;font-size:18px;font-weight:600;color:var(--dark);white-space:nowrap}
.caption p{position:absolute;left:16px;top:40px;font-size:12px;font-style:italic;color:#55616b;white-space:nowrap}
.caption .go{position:absolute;left:338px;top:10px;width:53px;height:51px;border-radius:8px;background:var(--light)}

/* trust */
.why h2{position:absolute;left:628px;top:2380px;font-size:32px;font-weight:500;line-height:42px;color:var(--dark)}
.why p{position:absolute;left:628px;width:460px;font-size:15.5px;line-height:24px;text-align:justify}
.why ul{position:absolute;left:628px;top:2650px;list-style:none;font-size:15.5px;line-height:29px;color:#2a3640}
.why li svg{vertical-align:-1px;margin-right:6px}

/* cta */
.cta{position:absolute;left:111px;top:2887px;width:978px;height:137px;border-radius:26px;background:var(--light);z-index:2}
.cta h2{position:absolute;left:46px;top:71px;font-size:31px;font-weight:700;color:var(--white)}
.cta .btn{left:773px;top:51px;width:158px;height:36px;background:var(--dark);box-shadow:0 2px 6px rgba(0,0,0,.25)}

/* footer */
.site-footer{position:absolute;left:0;top:2957px;width:1200px;height:379px;background:var(--dark);color:var(--white)}
.site-footer .brand{position:absolute;left:111px;top:155px;font-size:22px}
.foot-about{position:absolute;left:111px;top:219px;width:300px;font-size:14.5px;line-height:22px;color:#d7e2ea;text-align:justify}
.foot-col{position:absolute;top:145px}
.foot-col h4{font-size:19px;font-weight:600;margin-bottom:12px}
.foot-col li{list-style:none;font-size:14.5px;line-height:29px;color:#d7e2ea;white-space:nowrap}
.foot-col li svg{vertical-align:-1px;margin-right:12px}
.foot-line{position:absolute;left:111px;top:315px;width:978px;height:1px;background:rgba(255,255,255,.45)}
.copyright{position:absolute;left:0;top:332px;width:1200px;text-align:center;font-size:13px;color:#d7e2ea}
</style>
</head>
<body>

<header class="site-header">
  <div class="brand">Keelbrook Vault Holdings</div>
  <nav class="nav">
    <a class="active" href="#" style="left:698px">Home</a>
    <a href="#" style="left:789px">About</a>
    <a href="#" style="left:878px">Services</a>
    <span class="underline"></span>
  </nav>
  <a class="btn" href="#" style="left:984px;top:25px;width:145px;height:36px">Contact Us</a>
</header>

<!-- hero -->
<svg class="abs" style="left:0;top:85px" width="1200" height="630" viewBox="0 85 1200 630">
  <defs>
    <linearGradient id="heroFill" x1="0" y1="0" x2="1" y2="0">
      <stop offset="0" stop-color="#9fb6cf"/>
      <stop offset=".45" stop-color="#c9d5e4"/>
      <stop offset=".75" stop-color="#a89478"/>
      <stop offset="1" stop-color="#7d8a96"/>
    </linearGradient>
  </defs>
  <polygon role="img" aria-label="Photo: smiling staff member carrying a cardboard box in front of blue self storage doors" points="0,85 1200,85 1200,550 602,673 0,550" fill="url(#heroFill)"/>
  <polygon points="172,598 602,682 1010,598 602,710" fill="var(--dark)"/>
</svg>
<div class="hero-panel"></div>
<h1 class="hero-title"><span class="lead">From Concept to Capacity</span><span class="strong">Your Self Storage Experts</span></h1>
<p class="hero-text">Keelbrook Vault Holdings delivers turnkey design, construction, leasing &amp; management services for profitable self storage operations.</p>
<a class="btn" href="#" style="left:78px;top:427px;width:145px;height:36px">Learn More</a>

<div class="abs" role="img" aria-label="Decorative ring accent" style="left:70px;top:713px;width:120px;height:120px;border-radius:50%;background:radial-gradient(circle,rgba(43,170,223,0) 55%,rgba(43,170,223,.18) 56%,rgba(43,170,223,0) 72%)"></div>
<div class="abs" role="img" aria-label="Decorative striped accent" style="left:1036px;top:608px;width:142px;height:200px;background:linear-gradient(135deg,rgba(43,170,223,0),rgba(43,170,223,.16),rgba(43,170,223,0))"></div>

<!-- services -->
<svg class="roof" style="top:798px" viewBox="0 0 64 22"><polyline points="3,19 32,4 61,19" fill="none" stroke="var(--dark)" stroke-width="5"/></svg>
<h2 class="section-title" style="top:824px">Our <span>Services</span></h2>
<p class="intro">Lorem ipsum dolor sit amet, consectetur adipiscing elit, sed do eiusmod tempor incididunt ut labore et dolore magna aliqua. Quis ipsum suspendisse ultrices gravida risus commodo viverra maecenas</p>

<svg class="abs" style="left:0;top:980px" width="1200" height="311" viewBox="0 757 927 240">
  <g fill="none" stroke-width="2">
    <polyline points="223,762 110,762 87,812 110,862 310,862" stroke="var(--dark)"/>
    <line x1="310" y1="862" x2="373" y2="757" stroke="var(--light)"/>
    <polyline points="223,987 110,987 87,935 110,885 310,885" stroke="var(--dark)"/>
    <line x1="310" y1="885" x2="373" y2="990" stroke="var(--light)"/>
    <polyline points="705,762 810,762 840,812 810,862 615,862" stroke="var(--light)"/>
    <line x1="615" y1="862" x2="553" y2="757" stroke="var(--dark)"/>
    <polyline points="705,987 810,987 840,935 810,885 615,885" stroke="var(--light)"/>
    <line x1="615" y1="885" x2="553" y2="990" stroke="var(--dark)"/>
    <polygon points="400,764 527,764 597,874 527,985 400,985 330,874" stroke="var(--light)" stroke-dasharray="5 4" stroke-width="1.5"/>
    <polygon points="412,780 515,780 580,875 515,970 412,970 348,875" stroke="var(--dark)" stroke-linejoin="round"/>
  </g>
  <g>
    <circle cx="139" cy="815" r="31" fill="var(--light)"/>
    <circle cx="139" cy="933" r="31" fill="var(--light)"/>
    <circle cx="648" cy="815" r="31" fill="var(--dark)"/>
    <circle cx="648" cy="933" r="31" fill="var(--light)"/>
    <g fill="none" stroke="#fff" stroke-width="2">
      <path d="M126,829 V810 L139,801 L152,810 V829 Z M134,829 V817 H144 V829"/>
      <path d="M124,948 V927 L139,918 L154,927 V948 Z M131,942 L147,930 M131,930 L147,942"/>
      <path d="M634,830 V810 L648,801 L662,810 V830 Z M639,815 H657 M639,820 H657 M639,825 H657"/>
      <path d="M636,950 V923 H660 V950 Z M642,935 L647,941 L655,931"/>
    </g>
  </g>
</svg>
<div class="abs" style="left:450px;top:1112px;width:301px;text-align:center;font-size:24px;font-weight:600;line-height:29px;color:var(--dark)">Keelbrook Vault<br>Holdings</div>

<h3 class="service-title" style="left:234px;top:1012px">Facility Design &amp;<br>Development</h3>
<p class="service-note" style="left:235px;top:1062px">Strategic planning for<br>profitable facilities.</p>
<h3 class="service-title" style="left:234px;top:1165px">Construction &amp;<br>Build Management</h3>
<p class="service-note" style="left:235px;top:1215px">Quality-focused<br>construction oversight.</p>
<h3 class="service-title alt" style="left:894px;top:1012px">Lease-Up &amp;<br>Marketing</h3>
<p class="service-note" style="left:896px;top:1062px">Proven strategies to<br>accelerate occupancy.</p>
<h3 class="service-title" style="left:894px;top:1165px">Ongoing Facility<br>Management</h3>
<p class="service-note" style="left:896px;top:1215px">Maximizing revenue<br>with expert operations.</p>

<a class="btn" href="#" style="left:527px;top:1324px;width:145px;height:37px">Learn More</a>

<!-- projects -->
<section class="projects"></section>
<svg class="roof" style="top:1533px" viewBox="0 0 64 22"><polyline points="3,19 32,4 61,19" fill="none" stroke="var(--dark)" stroke-width="5"/></svg>
<h2 class="section-title" style="top:1561px">Our <span>Projects</span></h2>

<article class="project" style="left:111px">
  <div class="photo" role="img" aria-label="Photo: row of red self storage doors under a blue sky" style="background:linear-gradient(180deg,#6f9fd6 0%,#a9c3e0 22%,#c8ab86 32%,#d2362f 45%,#c9272a 100%)"></div>
  <div class="caption"><h3>Ridgeline Storage – Calgary, AB</h3><p>60,000 sq. ft. | 95% occupancy in 9 months</p>
    <span class="go"><svg width="53" height="51" viewBox="0 0 53 51"><path d="M19,33 L34,18 M22,18 H34 V30" fill="none" stroke="#fff" stroke-width="2.4"/></svg></span></div>
</article>
<article class="project" style="left:595px">
  <div class="photo" role="img" aria-label="Photo: blue-roofed self storage buildings with light blue doors" style="background:linear-gradient(180deg,#4e82c4 0%,#9cbbe0 30%,#2f6fb0 38%,#c9ccd0 55%,#8a9096 100%)"></div>
  <div class="caption"><h3>Harlow Storage – Calgary, AB</h3><p>53,000 sq. ft. | 92% occupancy in 7 months</p>
    <span class="go"><svg width="53" height="51" viewBox="0 0 53 51"><path d="M19,33 L34,18 M22,18 H34 V30" fill="none" stroke="#fff" stroke-width="2.4"/></svg></span></div>
</article>
<article class="project" style="left:1080px">
  <div class="photo" role="img" aria-label="Photo: self storage units with red doors and yellow bollard" style="background:linear-gradient(180deg,#3f78c7 0%,#8fb4e0 30%,#b84141 45%,#c6c0b8 100%)"></div>
  <div class="caption"><h3>Northgate Storage – Calgary, AB</h3><p>70,000 sq. ft. | 90% occupancy in 8 months</p></div>
</article>

<a class="btn" href="#" style="left:502px;top:2032px;width:196px;height:37px">View More Projects</a>

<!-- trust builder -->
<svg class="roof" style="top:2241px" viewBox="0 0 64 22"><polyline points="3,19 32,4 61,19" fill="none" stroke="var(--dark)" stroke-width="5"/></svg>
<h2 class="section-title" style="top:2268px">Trust <span>Builder</span></h2>
<div class="abs" role="img" aria-label="Decorative striped circle" style="left:1010px;top:2237px;width:142px;height:142px;border-radius:50%;background:rgba(43,170,223,.14)"></div>

<svg class="abs" style="left:100px;top:2362px" width="478" height="448" viewBox="100 2362 478 448" role="img" aria-label="Photo: businessman with a tablet in front of red storage doors">
  <defs>
    <linearGradient id="trustFill" x1="0" y1="0" x2="1" y2="0">
      <stop offset="0" stop-color="#8fb2d8"/>
      <stop offset=".45" stop-color="#5f7fa6"/>
      <stop offset=".6" stop-color="#c8343a"/>
      <stop offset="1" stop-color="#d9474b"/>
    </linearGradient>
  </defs>
  <polygon points="339,2385 555,2487 555,2685 339,2787 123,2685 123,2487" fill="url(#trustFill)" stroke="url(#trustFill)" stroke-width="24" stroke-linejoin="round"/>
</svg>

<div class="why">
  <h2>Why Choose Keelbrook Vault<br>Holdings?</h2>
  <p style="top:2486px">Lorem ipsum dolor sit amet, consectetur adipiscing elit, sed do eiusmod tempor incididunt ut labore et dolore magna aliqua. Quis ipsum suspendisse ultrices gravida. Risus commodo viverra maecenas</p>
  <p style="top:2588px">Sed ut perspiciatis unde omnis iste natus error sit volu ptatem accusantium doloremque</p>
  <ul>
    <li><svg width="14" height="12" viewBox="0 0 14 12"><path d="M1,1 L6,6 L1,11 M7,1 L12,6 L7,11" fill="none" stroke="var(--dark)" stroke-width="2"/></svg>Industry-leading self storage expertise</li>
    <li><svg width="14" height="12" viewBox="0 0 14 12"><path d="M1,1 L6,6 L1,11 M7,1 L12,6 L7,11" fill="none" stroke="var(--dark)" stroke-width="2"/></svg>Proven track record in lease-up success</li>
    <li><svg width="14" height="12" viewBox="0 0 14 12"><path d="M1,1 L6,6 L1,11 M7,1 L12,6 L7,11" fill="none" stroke="var(--dark)" stroke-width="2"/></svg>Strong vendor &amp; contractor network</li>
  </ul>
  <a class="btn" href="#" style="left:628px;top:2747px;width:145px;height:35px">Learn More</a>
</div>

<!-- call to action -->
<section class="cta">
  <svg class="abs" style="left:47px;top:30px" width="64" height="22" viewBox="0 0 64 22"><polyline points="3,19 32,4 61,19" fill="none" stroke="var(--dark)" stroke-width="5"/></svg>
  <h2>Let’s Build Your Storage Success.</h2>
  <a class="btn" href="#">Contact Us <svg style="margin-left:8px" width="18" height="12" viewBox="0 0 18 12"><path d="M1,6 H16 M11,1 L16,6 L11,11" fill="none" stroke="#fff" stroke-width="2"/></svg></a>
</section>

<!-- footer -->
<footer class="site-footer">
  <div class="brand">Keelbrook Vault Holdings</div>
  <p class="foot-about">Lorem ipsum dolor sit amet, consec te tur ad ip iscing elit, sed do eiusm od tem por incid idunt utlabore</p>
  <div class="foot-col" style="left:461px">
    <h4>Quick Links</h4>
    <ul>
      <li><svg width="8" height="12" viewBox="0 0 8 12"><path d="M1,1 L6,6 L1,11" fill="none" stroke="#fff" stroke-width="1.8"/></svg>Home</li>
      <li><svg width="8" height="12" viewBox="0 0 8 12"><path d="M1,1 L6,6 L1,11" fill="none" stroke="#fff" stroke-width="1.8"/></svg>About Us</li>
      <li><svg width="8" height="12" viewBox="0 0 8 12"><path d="M1,1 L6,6 L1,11" fill="none" stroke="#fff" stroke-width="1.8"/></svg>Services</li>
      <li><svg width="8" height="12" viewBox="0 0 8 12"><path d="M1,1 L6,6 L1,11" fill="none" stroke="#fff" stroke-width="1.8"/></svg>Contact Us</li>
    </ul>
  </div>
  <div class="foot-col" style="left:631px">
    <h4>Other Links</h4>
    <ul>
      <li><svg width="8" height="12" viewBox="0 0 8 12"><path d="M1,1 L6,6 L1,11" fill="none" stroke="#fff" stroke-width="1.8"/></svg>FAQs</li>
      <li><svg width="8" height="12" viewBox="0 0 8 12"><path d="M1,1 L6,6 L1,11" fill="none" stroke="#fff" stroke-width="1.8"/></svg>Terms &amp; Conditions</li>
      <li><svg width="8" height="12" viewBox="0 0 8 12"><path d="M1,1 L6,6 L1,11" fill="none" stroke="#fff" stroke-width="1.8"/></svg>Privacy Policy</li>
      <li><svg width="8" height="12" viewBox="0 0 8 12"><path d="M1,1 L6,6 L1,11" fill="none" stroke="#fff" stroke-width="1.8"/></svg>Sitemaps</li>
    </ul>
  </div>
  <div class="foot-col" style="left:858px">
    <h4>Contact Us</h4>
    <ul>
      <li style="line-height:21px;padding-top:4px"><svg width="12" height="15" viewBox="0 0 12 15" style="float:left;margin-top:3px"><path d="M6,14 C2,9 1,7 1,5 A5,5 0 0 1 11,5 C11,7 10,9 6,14 Z" fill="#fff"/><circle cx="6" cy="5" r="1.8" fill="var(--dark)"/></svg><span style="display:block;margin-left:29px">40837 52 Ave, Edmonton,<br>AB T6K 3R8</span></li>
      <li><svg width="14" height="11" viewBox="0 0 14 11"><rect x="0.5" y="0.5" width="13" height="10" fill="#fff"/><path d="M1,1 L7,6 L13,1" fill="none" stroke="var(--dark)" stroke-width="1.3"/></svg>info@keelbrookvault.net</li>
      <li><svg width="14" height="14" viewBox="0 0 14 14"><path d="M3,1 L5,1 L6,4 L4.5,5.5 C5.5,7.5 6.5,8.5 8.5,9.5 L10,8 L13,9 L13,11 C13,12 12,13 11,13 C6,13 1,8 1,3 C1,2 2,1 3,1 Z" fill="#fff"/></svg>+1 555-014-2290</li>
    </ul>
  </div>
  <div class="foot-line"></div>
  <p class="copyright">Copyright © 2025 Keelbrook Vault Holdings. All rights reserved.</p>
</footer>

</body>
</html>
```